Math Help Website Needs New Design

Looking to refresh the design of my existing site (quillnumberdesk.com) to be easier on the eyes. I am fully capable of doing the HTML coding and have for years, but I don't have the eye for good design, colors, layout, and fonts. This is where I need help!

I need both a new design scheme and a new logo that matches. The overall functionality will be the same as the existing site, and should not be unrecognizable.

Target Market(s)

It should appeal to students (age 13-22) and their parents, so it should NOT be childish in appearance, nor should it be corporate.

Requirements
Must have
• Should be simple, easy-to-navigate, and neither childish nor corporate. I am looking for a design for both the homepage and a similar "content" page. Simple, bold colors are preferred. A logo should be prominent at the top, with a search bar nearby. Below that I need a similar navigational area like I already have. Then, I need about 200px wide ad space on the left of the main body area.

```html
<!DOCTYPE html>
<html lang="en">
<head>
<meta charset="utf-8">
<title>Quill Number Desk</title>
<link href="https://fonts.googleapis.com/css2?family=Ubuntu:wght@400;500;700&display=swap" rel="stylesheet">
<style>
:root{
  --sky:#5b8fd6;
  --sky-light:#cfe0f6;
  --orange:#f07d1a;
  --page:#f2f4f7;
  --line:#dfe3e8;
  --text:#444;
  --heading:#333;
  --red:#c8161c;
  --red-dark:#9c0f13;
  --tab:#8cc3ea;
  --tab-active:#4f95d3;
  --footer:#2e3033;
  --green:#8dc641;
}
*{box-sizing:border-box;margin:0;padding:0}
html,body{width:895px;height:1200px;overflow:hidden;background:var(--page)}
body{font-family:"Ubuntu",sans-serif;color:var(--text);position:relative}
.abs{position:absolute}

.header{left:0;top:0;width:895px;height:72px;background:var(--sky)}
.header-stripe{left:0;top:72px;width:895px;height:6px;background:var(--orange)}
.header-band{left:0;top:78px;width:895px;height:26px;background:var(--sky-light)}
.brand{left:82px;top:8px;width:178px;height:56px;border-radius:50%;background:#fff;display:flex;align-items:center;justify-content:center;gap:6px}
.brand-dot{width:10px;height:10px;border-radius:50%;background:var(--orange)}
.brand-name{font-size:15px;font-weight:700;color:#2a4f9c}
.search{left:558px;top:14px;width:248px;height:16px;display:flex}
.search input{flex:1;border:0;padding-left:30px;font:8px "Ubuntu",sans-serif;color:#999;background:#fff}
.search button{width:47px;border:0;background:var(--green);color:#fff;font:8px "Ubuntu",sans-serif}
.nav{left:340px;top:46px;width:468px;height:32px;background:#fff;border-radius:10px 0 0 0;display:flex;align-items:center;padding-left:22px;font-size:8.6px;color:#333}
.nav a{color:inherit;text-decoration:none;padding:0 7px;border-left:1px solid var(--line);line-height:26px}
.nav a:first-child{border-left:0}

.slider{left:70px;top:86px;width:736px;height:292px;background:#fff;border:1px solid var(--line)}
.slide{left:13px;top:13px;width:711px;height:263px;background:linear-gradient(100deg,#e8e0d2 0%,#b69a72 35%,#6d4b2c 70%,#2e1a0e 100%)}
.slide-caption{left:0;bottom:0;width:100%;height:31px;background:rgba(40,30,20,.55);color:#fff;font-size:11.5px;line-height:31px;padding-left:15px}
.slide-arrow{top:118px}

.ad{left:70px;top:394px;width:150px;height:152px;border:2px solid #ccc;background:linear-gradient(160deg,#f4f6ec,#d8e2d6 60%,#b8c3c0)}
.ad-title{left:12px;top:62px;font-size:11px;color:#222;font-weight:500}
.ad-btn{left:33px;top:96px;width:88px;height:18px;border-radius:9px;background:var(--orange);color:#6a2d00;font-size:8.5px;text-align:center;line-height:18px}

.grades{left:70px;top:552px;width:150px}
.grade{height:24px;margin-bottom:6.6px;border-radius:7px;background:linear-gradient(#fafafa,#d4d4d4);border:1px solid #c8c8c8;font-size:8.8px;color:#333;line-height:22px;padding-left:22px}
.grade.active{background:var(--red);border-color:var(--red);color:#fff}

.study{left:70px;top:892px;width:150px;height:200px;background:#fff;border-radius:8px;padding:12px 6px}
.study h3{font-size:12px;font-weight:400;color:var(--heading);margin:0 0 10px 12px}
.study-item{display:flex;gap:5px;font-size:8.2px;line-height:13.5px;margin-bottom:12px}
.avatar{width:19px;height:19px;flex:none;background:#b7aaa0}

.welcome{left:239px;top:393px;width:565px;height:419px;background:#fff;border:1px solid var(--line);border-radius:6px;padding:19px 22px}
.welcome h2{font-size:13px;font-weight:400;color:var(--heading);margin-bottom:10px}
.welcome p{font-size:7.9px;line-height:16px;margin-bottom:15px}
.welcome p span{font-size:9.2px;color:#333}
.col{position:absolute;top:147px}
.col h3{font-size:12px;font-weight:400;color:var(--heading);margin-bottom:8px}
.col ul{list-style:none;font-size:8.6px}
.col li{line-height:15.6px;padding-left:14px;position:relative}
.col li::before{content:"›";position:absolute;left:2px;color:#555}
.col.disc ul{font-size:7.9px}
.col.disc li{padding-left:16px}

.tabs{left:241px;top:825px;width:563px;height:23px;display:flex;gap:2px}
.tab{flex:1;background:linear-gradient(#a7d4f1,var(--tab));border-radius:6px 6px 0 0;font-size:8.6px;color:#2b4e70;text-align:center;line-height:23px}
.tab.active{background:var(--tab-active);color:#fff}
.tool{left:239px;top:848px;width:565px;height:246px;background:#fff;border:1px solid var(--line);border-radius:0 0 6px 6px}
.icons{left:73px;width:400px;display:flex;justify-content:space-between}
.lbl{font-size:8.6px;color:#333}
.field{background:#fff;border:1px solid #c9c9c9}
.examples{font:7.6px Arial,sans-serif;color:#2a56a8;padding:2px 4px;line-height:13.5px;overflow:hidden}
.examples div::before{content:"+";display:inline-block;width:8px;height:8px;border:1px solid #777;color:#333;font-size:7px;line-height:7px;text-align:center;margin-right:3px}
.btn{background:linear-gradient(#e0262c,var(--red-dark));color:#fff;border-radius:7px;text-align:center;font-size:12px;font-weight:500}

.footer{left:0;top:1110px;width:895px;height:90px;background:var(--footer);border-top:2px solid #555}
.footer h3{position:absolute;left:75px;top:12px;font-size:12px;font-weight:400;color:#fff}
.email{left:72px;top:44px;width:165px;height:24px;background:#fff;border-radius:3px;font-size:8.8px;color:#888;padding:6px 10px}
.subscribe{left:254px;top:44px;width:64px;height:24px;background:var(--red);border-radius:3px;color:#fff;font-size:10px;font-weight:500;text-align:center;line-height:24px}
.social{left:638px;top:21px;display:flex;gap:13px}
.social span{width:16px;height:16px;border-radius:2px}
.copy{right:121px;top:56px;font-size:8px;color:#ddd}
</style>
</head>
<body>

<div class="abs header"></div>
<div class="abs header-stripe"></div>
<div class="abs header-band"></div>
<div class="abs brand"><span class="brand-dot"></span><span class="brand-name">Quill Number Desk</span></div>
<form class="abs search"><input value="type your word here" aria-label="Search"><button type="button">SEARCH</button></form>
<nav class="abs nav">
  <a>Home</a><a>Algebra</a><a>Geometry</a><a>Trig</a><a>Calculus</a><a>Statistics</a><a>More Subjects</a><a>Message Board</a>
</nav>

<div class="abs slider">
  <div class="abs slide" role="img" aria-label="Photo of geometry tools: compass, protractor, ruler and wooden solids on an open book">
    <svg class="abs slide-arrow" style="left:5px" width="18" height="36" viewBox="0 0 18 36"><path d="M15 2 L4 18 L15 34" fill="none" stroke="#fff" stroke-width="4"/></svg>
    <svg class="abs slide-arrow" style="right:12px" width="18" height="36" viewBox="0 0 18 36"><path d="M3 2 L14 18 L3 34" fill="none" stroke="#fff" stroke-width="4"/></svg>
    <div class="abs slide-caption">MATH LESSONS</div>
  </div>
</div>

<aside>
  <div class="abs ad" role="img" aria-label="Advert image of a student writing an exponent formula on a whiteboard">
    <div class="abs ad-title">QUILL NUMBER DESK</div>
    <div class="abs ad-btn">CLICK HERE</div>
  </div>
  <div class="abs grades">
    <div class="grade active">Kindergarten</div>
    <div class="grade">First Grade</div>
    <div class="grade">Second Grade</div>
    <div class="grade">Third&nbsp; Grade</div>
    <div class="grade">Fourth Grade</div>
    <div class="grade">Fifth Grade</div>
    <div class="grade">Sixth Grade</div>
    <div class="grade">Seventh Grade</div>
    <div class="grade">Eighth Grade</div>
    <div class="grade">Algebra</div>
    <div class="grade">Geometry</div>
  </div>
  <div class="abs study">
    <h3>Live Study Group</h3>
    <div class="study-item"><span class="avatar" role="img" aria-label="Member avatar"></span><span>Solve the following system using the substitution method: 6x - 2y = -4 y = 3x + 2 12 replies</span></div>
    <div class="study-item"><span class="avatar" role="img" aria-label="Member avatar"></span><span>Solve the equation. 7(2b – 5) + 3 = 10 5 replies</span></div>
    <div class="study-item"><span class="avatar" style="background:#ccc" role="img" aria-label="Member avatar"></span><span>how to find a formal charge in organic chemis-try? 1 reply</span></div>
  </div>
</aside>

<main class="abs welcome">
  <h2>Welcome to Quill Number Desk</h2>
  <p><span>Math Lessons -</span> Looking to understand a subject better, or maybe you don't understand what your textbook is trying to tell you? We have a collection of algebra and geometry lessons that you can view online right now.</p>
  <p><span>Ask your question</span> on our math help message board. Just be sure to explain what you've tried to do and where you're stuck, and a friendly volunteer may try to assist you!</p>
  <div class="col" style="left:22px">
    <h3>What's New?</h3>
    <ul>
      <li>Multiplying Polynomials</li>
      <li>Derivative of an Inverse Function</li>
      <li>Derivatives of Logs and Exps</li>
      <li>Differentiating Trig Functions</li>
    </ul>
    <h3 style="margin-top:18px">Math Lessons</h3>
    <ul>
      <li>Algebra</li><li>Geometry</li><li>Trigonometry</li><li>Calculus</li><li>Statistics</li><li>Sports Math</li><li>Math Games</li><li>Calculators</li>
    </ul>
  </div>
  <div class="col disc" style="left:261px">
    <h3>Current Discussions</h3>
    <ul>
      <li>question relating to hcf,lcm and time... Posted by: tovin42</li>
      <li>Exponential growth question Posted by: euclidean</li>
      <li>Help!! metric units Posted by: JonR</li>
      <li>Calculating percentile and standard d... Posted by: DrLen</li>
      <li>Linear word problem Posted by: JonR</li>
      <li>Fleece boots offer... Posted by: MarcoQ</li>
      <li>More Arc Length Posted by: MarcoQ</li>
      <li>Split - same issue, I need major help... Posted by: Elsabetta</li>
      <li>Solving for a Constant Return to arri... Posted by: Elsabetta</li>
      <li>Help with percentage question!! Posted by: Suren Dalal</li>
      <li>Weighing puzzler Posted by: JonR</li>
      <li>Quiz Problem I got Wrong Posted by: lookback</li>
      <li>Need help with this Vector problem! Posted by: srmartin</li>
      <li>precalculus word problem Posted by: MarcoQ</li>
    </ul>
  </div>
</main>

<div class="abs tabs">
  <div class="tab active">Basic Math</div><div class="tab">Pre-Algebra</div><div class="tab">Algebra</div><div class="tab">Trigonometry</div><div class="tab">Precalculus</div><div class="tab">Statistics</div>
</div>
<section class="abs tool">
  <svg class="abs" style="left:73px;top:24px" width="400" height="44" viewBox="0 0 400 44" fill="none" stroke="#222" stroke-width="1.2">
    <g stroke="#2a4f9c" fill="#9fb9e6">
      <rect x="3" y="4" width="10" height="7"/><rect x="42" y="4" width="10" height="7"/><rect x="81" y="0" width="10" height="5"/><rect x="81" y="8" width="10" height="5"/><rect x="118" y="3" width="10" height="9"/><rect x="157" y="4" width="10" height="7"/><rect x="194" y="4" width="6" height="7"/><rect x="203" y="4" width="6" height="7"/><rect x="233" y="5" width="6" height="6"/>
    </g>
    <path d="M2 3 Q0 7.5 2 12 M14 3 Q16 7.5 14 12 M40 3 V12 M54 3 V12 M78 6.5 H94"/>
    <path d="M150 8 L152 12 L155 2 H168 M192 3 Q190 7.5 192 12 M211 3 Q213 7.5 211 12"/>
    <text x="240" y="12" font-size="6" fill="#222" stroke="none">-10</text>
    <path d="M275 2 L283 5 L275 8 M275 11 H283 M325 2 L317 5 L325 8 M317 11 H325 M360 7 H371"/>
    <circle cx="365.5" cy="3" r="1" fill="#222"/><circle cx="365.5" cy="11" r="1" fill="#222"/>
    <rect x="1" y="24" width="19" height="18"/>
    <circle cx="49" cy="33" r="10"/>
    <path d="M88 24 L99 42 H77 Z"/>
    <path d="M120 42 L125 26 H143 L138 42 Z"/>
    <path d="M169 26 H183 L188 42 H164 Z"/>
    <path d="M205 28 H222 V42 H205 Z M205 28 L210 24 H227 L222 28 M227 24 V38 L222 42"/>
    <ellipse cx="252" cy="27" rx="9" ry="3"/><path d="M243 27 V39 M261 27 V39"/><path d="M243 39 A9 3 0 0 0 261 39"/>
    <ellipse cx="292" cy="39" rx="10" ry="3"/><path d="M282 39 L292 23 L302 39"/>
    <path d="M330 23 L319 41 H343 Z M330 23 L336 36 L319 41 M336 36 L343 41"/>
    <circle cx="380" cy="33" r="10"/><ellipse cx="380" cy="33" rx="10" ry="3"/>
  </svg>
  <div class="abs lbl" style="left:32px;top:112px">Enter Problem :</div>
  <div class="abs field" style="left:107px;top:94px;width:164px;height:50px"></div>
  <div class="abs lbl" style="left:302px;top:112px">Examples:</div>
  <div class="abs field examples" style="left:361px;top:94px;width:164px;height:50px">
    <div>Long Arithmetic</div><div>Rational Numbers</div><div>Operations with Fractions</div><div>Ratios, Proportions, and Percents</div>
  </div>
  <div class="abs lbl" style="left:32px;top:176px">Math Format :</div>
  <div class="abs btn" style="left:111px;top:170px;width:86px;height:22px;line-height:22px">Show</div>
  <div class="abs lbl" style="left:302px;top:172px">Select Topic :</div>
  <div class="abs field" style="left:361px;top:166px;width:164px;height:24px">
    <svg class="abs" style="right:4px;top:6px" width="12" height="11" viewBox="0 0 12 11"><rect x=".5" y=".5" width="11" height="10" fill="#eee" stroke="#888"/><path d="M3 4 L9 4 L6 8 Z" fill="#222"/></svg>
  </div>
  <div class="abs btn" style="left:239px;top:214px;width:115px;height:24px;line-height:24px">Answer</div>
</section>

<footer class="abs footer">
  <h3>Subscribe to our Newsletter</h3>
  <div class="abs email">Email</div>
  <div class="abs subscribe">Subscribe</div>
  <div class="abs social">
    <span style="background:#3b5b9b"></span><span style="background:#3fa9df"></span><span style="background:#ef6a1e"></span><span style="background:#1a7bb5"></span><span style="background:#d9412f"></span>
  </div>
  <div class="abs copy">© 2013&nbsp; quillnumberdesk.com, All Right Reserved</div>
</footer>

</body>
</html>
```